Past Cedar Hills Oz Tour Flyer

I need a dynamic flyer for a concert tour.
I have uploaded the file. Please use these ingredients for the design.
The font for the title is Jellyka Jellyfish lower case from www.glyphmarket-demo.net
Updates
We are getting close!! We just need bright colours, the headings to STAND OUT and Byron Bay has to be moved to under NSW Bellingen.
Thanks for all your hard work!
Target Market(s)
We are targeting a wide range of customers from old age to children and families
Industry/Entity Type
Tour
Look and feel
Each slider illustrates characteristics of the customer's brand and the style your logo design should communicate.

```html
<!DOCTYPE html>
<html lang="en">
<head>
<meta charset="utf-8">
<title>Past Cedar Hills – Australia Tour</title>
<link rel="stylesheet" href="https://fonts.googleapis.com/css2?family=Cedarville+Cursive&family=Mulish:wght@400;800&family=Arimo:wght@400&display=swap">
<style>
  :root {
    --ink-dark: #1c0d05;
    --title-gold: #ffd54a;
    --band-red: #c8200e;
    --panel-gold: rgba(255, 208, 90, 0.84);
    --panel-black: #070403;
    --list-dark: #2e1407;
    --white: #ffffff;
  }
  * { margin: 0; padding: 0; box-sizing: border-box; }
  html, body { width: 846px; height: 1200px; overflow: hidden; background: var(--ink-dark); }
  .flyer { position: relative; width: 846px; height: 1200px; overflow: hidden; font-family: "Arimo", Arial, sans-serif; }

  .stage-photo {
    position: absolute; inset: 0;
    background:
      radial-gradient(ellipse 230px 300px at 440px 520px, rgba(255,190,40,0.95), rgba(255,140,20,0) 100%),
      radial-gradient(ellipse 300px 260px at 500px 800px, rgba(255,90,10,1), rgba(230,60,10,0) 100%),
      radial-gradient(ellipse 170px 300px at 790px 620px, rgba(255,170,40,0.9), rgba(230,90,20,0) 100%),
      radial-gradient(ellipse 120px 300px at 30px 600px, rgba(255,150,30,0.8), rgba(230,90,20,0) 100%),
      radial-gradient(ellipse 560px 440px at 640px 380px, #b08540 0%, #6a4520 55%, rgba(30,15,5,0) 100%),
      linear-gradient(180deg, #1f1108 0%, #4a2e14 35%, #3a1e0a 75%, #120804 100%);
  }

  .tour-title {
    position: absolute; left: 105px; top: 32px;
    font-family: "Cedarville Cursive", cursive;
    font-size: 92px; line-height: 1; color: var(--title-gold);
    letter-spacing: 2px; white-space: nowrap;
  }
  .choir-name {
    position: absolute; left: 127px; top: 158px;
    font-family: "Mulish", sans-serif; font-size: 31px; color: var(--white);
  }
  .choir-name strong { font-weight: 800; }

  .tour-band {
    position: absolute; left: 0; top: 213px; width: 352px; height: 49px;
    background: var(--band-red); color: var(--white);
    font-family: "Mulish", sans-serif; font-size: 30px; line-height: 49px; padding-left: 140px;
  }

  .venues { position: absolute; left: 78px; top: 372px; width: 212px; }
  .venues .cap { height: 12px; background: var(--band-red); }
  .region { padding: 20px 0 12px 26px; font-size: 21.5px; line-height: 28px; }
  .region p { white-space: nowrap; }
  .region--gold { background: var(--panel-gold); color: var(--list-dark); }
  .region--red { background: var(--band-red); color: var(--white); padding-top: 14px; padding-bottom: 14px; }
  .region--black { background: var(--panel-black); color: var(--white); padding-top: 12px; }
  .region--vic { height: 206px; }
  .region--act { height: 80px; }
  .region--nsw { height: 304px; padding-top: 12px; }
  .region--qld { height: 151px; }

  .tickets {
    position: absolute; left: 322px; top: 872px; width: 524px; height: 90px;
    background: var(--band-red); color: var(--white);
    font-size: 20.5px; line-height: 29px; padding: 16px 0 0 30px;
  }

  .partner {
    position: absolute; top: 962px; height: 163px;
    display: flex; align-items: center; justify-content: center; gap: 10px;
    font-family: "Mulish", sans-serif; font-weight: 800; font-size: 20px;
  }
  .partner--chorale { left: 322px; width: 180px; background: var(--panel-black); color: var(--title-gold); }
  .partner--choir { left: 505px; width: 280px; background: var(--white); color: var(--panel-black); }
  .partner .dot { width: 14px; height: 14px; border-radius: 50%; background: currentColor; flex: none; }
</style>
</head>
<body>
<main class="flyer">
  <div class="stage-photo" role="img" aria-label="Photograph of young choir members dancing on stage in bright orange and yellow costumes with grass skirts"></div>

  <h1 class="tour-title">Past Cedar Hills</h1>
  <p class="choir-name">The <strong>Riverstone Youth</strong> Choir</p>
  <div class="tour-band">Australia Tour</div>

  <section class="venues">
    <div class="cap"></div>
    <div class="region region--gold region--vic">
      <p>VICTORIA</p><p>Geelong</p><p>Sunbury</p><p>Melbourne</p><p>Bendigo</p><p>Albury</p>
    </div>
    <div class="region region--red region--act">
      <p>A.C.T.</p><p>Canberra</p>
    </div>
    <div class="region region--gold region--nsw">
      <p>N.S.W.</p><p>Nowra</p><p>Sydney</p><p>Wollongong</p><p>Blue Mountains</p><p>Port Macquarie</p><p>Laurieton</p><p>Taree</p><p>Bellingen</p><p>Byron Bay</p>
    </div>
    <div class="region region--black region--qld">
      <p>QLD</p><p>Gold Coast</p><p>Sunshine Coast</p><p>Brisbane</p>
    </div>
  </section>

  <div class="tickets">
    <p>TICKETS and info at www.chorale-link-demo.org</p>
    <p>CONTACT: Dana Welling&nbsp; 0400 555 218</p>
  </div>

  <div class="partner partner--chorale"><span class="dot"></span>Chorale Link</div>
  <div class="partner partner--choir"><span class="dot"></span>Riverstone Youth Choir</div>
</main>
</body>
</html>
```